Business Card for Mortuary

We need a business card design for our mortuary. We are not the "traditional" mortuary and specialize in simple cremations and burials. We use a two sided card.

Industry/Entity Type

Funeral Home

Contact Information for Business Card

One side we would like to have with the general information of the mortuary:
Address: 4172 E. Larkspur Ave, Sun City, AZ 85904
Phone: 623-555-0148
email: hello@willowmereplace.com
website: willowmereplace.com

On the other side would like to have the information of employee:
Name: Peter K. Lund
Email: peter@willowmereplace.com
Title: Funeral Director
Text: 602-555-0173

Font styles to use
Serif
Sans Serif

Requirements
Should not have
• Do not put any gothic images or things like a hearse or tombstone.

```html
<!DOCTYPE html>
<html lang="en">
<head>
<meta charset="utf-8">
<title>Willowmere Place – Business Card</title>
<link href="https://fonts.googleapis.com/css2?family=Poppins:wght@400;500;600;700&display=swap" rel="stylesheet">
<style>
  :root {
    --backdrop: #d7d7d7;
    --card: #ffffff;
    --ink: #1a1a1a;
    --green: #8cc63f;
    --green-soft: #b3d43a;
    --rule: #555555;
  }
  * { margin: 0; padding: 0; box-sizing: border-box; }
  html, body {
    width: 1200px; height: 800px; overflow: hidden;
    background: var(--backdrop);
    font-family: "Poppins", sans-serif;
    color: var(--ink);
  }
  .stage { position: relative; width: 1200px; height: 800px; }
  .card {
    position: absolute; top: 283px;
    width: 429px; height: 238px;
    background: var(--card);
  }
  .card--front { left: 111px; }
  .card--back { left: 638px; }
  .abs { position: absolute; white-space: nowrap; }

  /* employee side */
  .mini-mark { left: 25px; top: 118px; display: flex; align-items: center; gap: 7px; }
  .mark-dot { width: 30px; height: 30px; border-radius: 50%; background: var(--green-soft); flex: none; }
  .mini-mark .brand-name { font-size: 12px; font-weight: 600; color: var(--green); }
  .person { left: 25px; top: 189px; line-height: 13px; }
  .person__name { font-size: 12px; font-weight: 600; }
  .person__title { font-size: 10.5px; color: var(--green-soft); font-weight: 500; }
  .divider { left: 120px; top: 191px; width: 1px; height: 23px; background: var(--rule); }
  .contact { font-size: 10.5px; line-height: 14px; }
  .contact li { list-style: none; display: flex; align-items: center; gap: 6px; }
  .contact svg { width: 8px; height: 8px; fill: var(--green); flex: none; }
  .card--front .contact { left: 130px; top: 188px; }

  /* company side */
  .brand-dot { left: 32px; top: 34px; width: 46px; height: 46px; border-radius: 50%; background: var(--green-soft); }
  .brand { left: 86px; top: 67px; display: flex; align-items: center; gap: 5px; }
  .brand-lockup {
    font-size: 18px; font-weight: 700;
    line-height: 19px; letter-spacing: -0.2px; color: var(--ink);
  }
  .tagline {
    padding-left: 3px;
    border-left: 1px solid var(--green);
    font-size: 10.5px; line-height: 13px; color: var(--green);
  }
  .card--back .contact { left: 32px; top: 170px; }
  .address { right: 31px; top: 170px; text-align: right; font-size: 10.5px; line-height: 14px; font-style: normal; }
</style>
</head>
<body>
<main class="stage">
  <section class="card card--front" aria-label="Employee side">
    <div class="abs mini-mark"><span class="mark-dot"></span><span class="brand-name">Willowmere Place</span></div>
    <div class="abs person">
      <p class="person__name">Peter K. Lund</p>
      <p class="person__title">Funeral Director</p>
    </div>
    <span class="abs divider"></span>
    <ul class="abs contact">
      <li><svg viewBox="0 0 10 10"><path d="M2 0.5l2 2-1 1.3c.6 1.3 1.6 2.3 2.9 2.9L7.2 5.7l2.3 2-1 1.8C4.4 9.5.5 5.6.5 1.5z"/></svg>Text : 602-555-0173</li>
      <li><svg viewBox="0 0 10 10"><path d="M0 2h10v6H0z M0 2l5 3.3L10 2" stroke="#fff" stroke-width=".8"/></svg>peter@willowmereplace.com</li>
    </ul>
  </section>

  <section class="card card--back" aria-label="Company side">
    <span class="abs brand-dot"></span>
    <div class="abs brand">
      <div class="brand-lockup">WILLOWMERE<br>PLACE</div>
      <div class="tagline">Affordable<br>Cremation<br>and Burial</div>
    </div>
    <ul class="abs contact">
      <li><svg viewBox="0 0 10 10"><path d="M2 0.5l2 2-1 1.3c.6 1.3 1.6 2.3 2.9 2.9L7.2 5.7l2.3 2-1 1.8C4.4 9.5.5 5.6.5 1.5z"/></svg>623-555-0148</li>
      <li><svg viewBox="0 0 10 10"><path d="M0 2h10v6H0z M0 2l5 3.3L10 2" stroke="#fff" stroke-width=".8"/></svg>hello@willowmereplace.com</li>
      <li><svg viewBox="0 0 10 10"><circle cx="5" cy="5" r="4.3" fill="none" stroke="#8cc63f" stroke-width="1.2"/><path d="M.8 5h8.4M5 .8c-2.2 2.5-2.2 5.9 0 8.4M5 .8c2.2 2.5 2.2 5.9 0 8.4" fill="none" stroke="#8cc63f" stroke-width=".9"/></svg>willowmereplace.com</li>
    </ul>
    <address class="abs address">4172 E. Larkspur Ave<br>Sun City, AZ 85904</address>
  </section>
</main>
</body>
</html>
```